Design a refer a friend Flyer (French & English)
Flyer Title:
Main Title: "Refer a Friend & Receive a Free Electric Toothbrush!"
Bold and clear, centered at the top.
Use a clean and modern font.
Color: White text on a vivid green background for maximum contrast and readability.
Visual Focus:
Toothbrush Image: Place a high-quality image of the Dentiva Glide 300 Electric Toothbrush in the center of the flyer.
Include a small price tag with “Value of $50” near the toothbrush to highlight the reward.
Simple Message:
Text: "Refer a friend to Centre Dentaire Val-Fleuri. When they book and attend their appointment, you get a free electric toothbrush, and they receive a special gift!"
Straightforward and easy to understand.
Placed below the image of the toothbrush.
Referral Process:
3 Easy Steps:
Refer a Friend
They Book and Come to Their Appointment
Receive Your Free Electric Toothbrush
Use simple, minimal icons to visually represent each step.
Keep the steps aligned horizontally or vertically for clarity.
Call to Action:
Text: "Start Referring Today!"
Place it in a button-like design in the vivid green color with bold, white text to make it stand out.
Contact Information:
Details:
Logo of Centre Dentaire Val-Fleuri.
Address: "48 Rue Lambert Ouest, Suite 210".
Phone Number and Website: Positioned at the bottom for easy reference.
Color Scheme:
Use a vivid green background for the entire flyer, with white accents for text and icons to maintain a fresh, clean look.
Minimal clutter, focusing on clarity and the key elements: the toothbrush, the call to action, and contact information.
Clinic : www.cdvalfleuri-example.com
Attached is the brandbook, logo and inspo I made with AI.
French text will be provided.
Thank you,
Idris

```html
<!DOCTYPE html>
<html lang="en">
<head>
<meta charset="UTF-8">
<title>Refer a Friend – Centre Dentaire Val-Fleuri</title>
<link rel="stylesheet" href="https://fonts.googleapis.com/css2?family=Roboto:wght@500;700;900&display=swap">
<style>
  :root {
    --green-deep: #13984a;
    --green-main: #1eab56;
    --green-light: #4cc47a;
    --white: #ffffff;
    --white-soft: rgba(255,255,255,0.55);
    --brush-top: #e9f3fb;
    --brush-mid: #c9dcea;
    --brush-dark: #2a2f33;
  }
  * { margin: 0; padding: 0; box-sizing: border-box; }
  html, body { width: 927px; height: 1200px; overflow: hidden; }
  body { font-family: "Roboto", Arial, sans-serif; color: var(--white); }

  .flyer {
    position: relative;
    width: 927px;
    height: 1200px;
    overflow: hidden;
    background:
      radial-gradient(circle at 85% 45%, rgba(140,230,170,0.45) 0%, rgba(140,230,170,0) 45%),
      linear-gradient(160deg, var(--green-deep) 0%, var(--green-main) 55%, var(--green-light) 100%);
  }

  .headline { position: absolute; left: 78px; top: 48px; line-height: 0.95; font-weight: 700; }
  .headline__refer { display: block; font-size: 103px; letter-spacing: -1px; }
  .headline__receive { display: block; font-size: 70px; margin-top: 6px; }
  .headline__reward { display: block; font-size: 97px; margin-top: 8px; }

  .intro {
    position: absolute; left: 80px; top: 428px; width: 550px;
    font-size: 17.5px; font-weight: 700; line-height: 1.5;
  }

  .steps-wrap { position: absolute; left: 80px; top: 545px; width: 560px; }
  .steps__line {
    position: absolute; left: 9px; top: 34px; width: 2px; height: 205px;
    background: var(--white-soft);
  }
  .steps { list-style: none; position: relative; }
  .step { position: relative; display: flex; align-items: center; margin-bottom: 28px; min-height: 80px; }
  .step__dot {
    position: absolute; left: 3px; width: 14px; height: 14px; border-radius: 50%;
    background: var(--white);
  }
  .step__icon { width: 56px; height: 56px; margin-left: 62px; flex: none; }
  .step__label { margin-left: 34px; font-size: 29px; font-weight: 700; line-height: 1.2; }

  .cta {
    position: absolute; left: 71px; top: 874px; width: 553px; height: 88px;
    border: 3px solid var(--white); border-radius: 44px;
    display: flex; align-items: center; justify-content: center;
    font-size: 38px; font-weight: 700;
  }

  .clinic-name {
    position: absolute; left: 80px; top: 1005px; font-weight: 700; line-height: 1.1;
    display: flex; align-items: center; gap: 30px;
  }
  .clinic-name__title { display: block; font-size: 54px; }
  .clinic-name__place { display: block; font-size: 21px; margin-top: 8px; }
  .clinic-name__mark { width: 56px; height: 56px; border-radius: 50%; background: var(--white); flex: none; }

  .contact {
    position: absolute; left: 80px; top: 1130px;
    font-size: 19px; font-weight: 500; display: flex; gap: 11px; white-space: nowrap;
  }
  .contact__sep { color: var(--white-soft); }

  .product-visual {
    position: absolute; left: 668px; top: 150px; width: 240px; height: 930px;
    border-radius: 120px 120px 60px 60px;
    background: linear-gradient(180deg, var(--brush-top) 0%, var(--brush-mid) 45%, var(--brush-dark) 62%, #1a1d20 100%);
    opacity: 0.92;
  }
  .value-tag {
    position: absolute; left: 812px; top: 760px; font-weight: 700; line-height: 1;
  }
  .value-tag__label { display: block; font-size: 14px; }
  .value-tag__price { display: block; font-size: 34px; margin-top: 4px; }
</style>
</head>
<body>
<main class="flyer">
  <h1 class="headline">
    <span class="headline__refer">REFER A FRIEND</span>
    <span class="headline__receive">&amp; Receive a</span>
    <span class="headline__reward">Free Electric<br>Toothbrush!</span>
  </h1>

  <p class="intro">Refer a friend to Centre Dentaire Val-Fleuri. When they book and attend their appointment, you get a free electric toothbrush, and they receive a special gift!</p>

  <div class="steps-wrap">
    <div class="steps__line" aria-hidden="true"></div>
    <ol class="steps">
      <li class="step">
        <span class="step__dot"></span>
        <svg class="step__icon" viewBox="0 0 56 56" fill="none" stroke="#fff" stroke-width="3" stroke-linecap="round" stroke-linejoin="round" aria-hidden="true">
          <circle cx="24" cy="17" r="9"/>
          <path d="M8 46c0-9 7-15 16-15 4 0 7 1 10 3"/>
          <path d="M36 46c2-6 6-9 12-9"/>
          <path d="M44 33l5 4-5 4"/>
        </svg>
        <span class="step__label">Refer a Friend</span>
      </li>
      <li class="step">
        <span class="step__dot"></span>
        <svg class="step__icon" viewBox="0 0 56 56" fill="none" stroke="#fff" stroke-width="3" stroke-linecap="round" stroke-linejoin="round" aria-hidden="true">
          <rect x="6" y="10" width="36" height="34" rx="4"/>
          <path d="M6 20h36M15 5v9M33 5v9"/>
          <circle cx="40" cy="40" r="10" fill="#1eab56"/>
          <path d="M35 40l4 4 6-7"/>
        </svg>
        <span class="step__label">They Book and Come to<br>Their Appointment</span>
      </li>
      <li class="step">
        <span class="step__dot"></span>
        <svg class="step__icon" viewBox="0 0 56 56" fill="none" stroke="#fff" stroke-width="3" stroke-linecap="round" stroke-linejoin="round" aria-hidden="true">
          <path d="M10 48l22-22 6 6-22 22z" transform="translate(-2,-4)"/>
          <path d="M34 20l8-8 4 4-8 8z"/>
          <path d="M43 9l4-4"/>
          <circle cx="17" cy="41" r="1.5" fill="#fff"/>
        </svg>
        <span class="step__label">Receive Your Free<br>Electric Toothbrush</span>
      </li>
    </ol>
  </div>

  <div class="cta">Start Referring Today!</div>

  <div class="clinic-name">
    <span>
      <span class="clinic-name__title">Clinique Dentaire</span>
      <span class="clinic-name__place">Val-Fleuri</span>
    </span>
    <span class="clinic-name__mark" aria-hidden="true"></span>
  </div>

  <p class="contact">
    <span>48 Rue Lambert Ouest, Suite 210</span>
    <span class="contact__sep">/</span>
    <span>www.cdvalfleuri-example.com</span>
    <span class="contact__sep">/</span>
    <span>514-555-0142</span>
  </p>

  <div class="product-visual" role="img" aria-label="Photo of the Dentiva Glide 300 electric toothbrush standing upright with a round brush head"></div>
  <div class="value-tag">
    <span class="value-tag__label">VALUE OF</span>
    <span class="value-tag__price">$50</span>
  </div>
</main>
</body>
</html>
```